Book on emotional dysfunction needs a book cover

This book, entitled "Inner Turmoil and the Scented Memory Path", by Darren Holloway, needs a front cover. The cover could possibly show an adult who is really a child, or a person actively smelling who not really there, like in an alternate dimension.

```html
<!DOCTYPE html>
<html lang="en">
<head>
<meta charset="utf-8">
<title>Inner Turmoil and the Scented Memory Path — Book Cover</title>
<link rel="stylesheet" href="https://fonts.googleapis.com/css2?family=Bebas+Neue&family=Roboto+Slab:wght@300;700&display=swap">
<style>
  :root {
    --backdrop-light: #ffffff;
    --backdrop-dark: #e4e4e4;
    --cover-top: #4c4c4e;
    --cover-bottom: #38383a;
    --ink-white: #ffffff;
    --ink-red: #e8141c;
  }
  * { margin: 0; padding: 0; box-sizing: border-box; }
  html, body {
    width: 1200px;
    height: 800px;
    overflow: hidden;
  }
  body {
    background: radial-gradient(ellipse at 50% 45%, var(--backdrop-light) 30%, var(--backdrop-dark) 100%);
    position: relative;
  }
  .book-cover {
    position: absolute;
    left: 410px;
    top: 100px;
    width: 380px;
    height: 600px;
    background: linear-gradient(160deg, var(--cover-top), var(--cover-bottom));
    display: flex;
    flex-direction: column;
    align-items: center;
    padding-top: 78px;
  }
  .title {
    font-family: "Bebas Neue", "Arial Narrow", sans-serif;
    font-weight: 400;
    color: var(--ink-white);
    text-align: center;
    line-height: 0.92;
    font-size: 60px;
    letter-spacing: 0.5px;
  }
  .title-line { display: block; }
  .title-line--ruled {
    display: flex;
    align-items: center;
    justify-content: center;
    gap: 12px;
  }
  .rule {
    display: inline-block;
    width: 62px;
    height: 15px;
    background: repeating-linear-gradient(
      to bottom,
      var(--ink-white) 0 2px,
      transparent 2px 6.5px
    );
    margin-top: -4px;
  }
  .title-line--accent {
    color: var(--ink-red);
    font-size: 132px;
    line-height: 0.9;
    margin-top: 10px;
    letter-spacing: 2px;
  }
  .author {
    position: absolute;
    bottom: 46px;
    left: 0;
    right: 0;
    text-align: center;
    font-family: "Roboto Slab", Georgia, serif;
    color: var(--ink-white);
    font-size: 19px;
    letter-spacing: 0.5px;
  }
  .author-by { font-weight: 300; margin-right: 4px; }
  .author-name { font-weight: 700; }
</style>
</head>
<body>
  <main class="book-cover">
    <h1 class="title">
      <span class="title-line">Inner</span>
      <span class="title-line">Turmoil</span>
      <span class="title-line title-line--ruled"><span class="rule"></span>And the<span class="rule"></span></span>
      <span class="title-line">Scented Memory</span>
      <span class="title-line title-line--accent">Path</span>
    </h1>
    <p class="author"><span class="author-by">BY</span> <span class="author-name">DARREN HOLLOWAY</span></p>
  </main>
</body>
</html>
```